BrimPath Tri-Fold Design & Box Layout

Need Tri-Fold Design for new brand called BrimPath Wireless. The design should be based on colors, logo, and text copy on www.brimpathwireless-demo.com See uploads for templates to use and ask questions. I am very responsive. Also need artwork for mobile phone box to go with the flyer design concept. The box can be very generic but same color theme, etc. with logo.

Target Market(s)

all types of people but focused on the sub-prime market.

Industry/Entity Type

Wireless Communication

Font styles to use
Serif
Sans Serif

Colors
33a6d7
abd036
f78f20

Requirements
Must have
• tri-fold and box layout using provided templates. do not outline any text as we may want to update before going to print. See layout for Tri-Fold as some will be English and some Spanish. Its OK if you just duplicate the English and we will translate as needed.
Nice to have
• Colors in Logo are:
• Green - #C5D42D
• Orange - #F6941F
• Blue - #58BAE9
Should not have
• no images of people.

```html
<!DOCTYPE html>
<html lang="en">
<head>
<meta charset="utf-8">
<title>BrimPath Wireless Tri-Fold</title>
<link href="https://fonts.googleapis.com/css2?family=Oswald:wght@400;500&family=Lato:wght@400;700&display=swap" rel="stylesheet">
<style>
:root{
  --blue:#33a6d7;
  --blue-deep:#1f7fc0;
  --green:#abd036;
  --green-text:#8fb31e;
  --orange:#f78f20;
  --ink:#333;
  --muted:#555;
  --stage:#4a4a4a;
}
*{box-sizing:border-box;margin:0;padding:0}
html,body{width:1200px;height:2695px;overflow:hidden;background:var(--stage)}
body{position:relative;font-family:'Lato',sans-serif;color:var(--ink)}
.spread{position:absolute;left:248px;width:745px;height:784px;background:#fff;box-shadow:0 4px 14px rgba(0,0,0,.35);overflow:hidden}
.spread-cover{top:84px}.spread-inside-en{top:952px}.spread-inside-es{top:1820px}
.panel{position:absolute;top:0;width:372px;height:100%}
.panel-left{left:0;background:linear-gradient(90deg,#fff 72%,#e2e2e2)}
.panel-right{left:372px;width:373px;background:#fff}
.url-band{position:absolute;left:0;right:0;bottom:0;height:60px;display:flex;align-items:center;justify-content:center;color:#fff;font-weight:700;font-size:15px;letter-spacing:2px;z-index:3}
.band-blue{background:linear-gradient(90deg,var(--blue-deep),var(--blue))}
.band-orange{background:var(--orange)}
.brand{position:absolute;left:0;right:0;display:flex;align-items:center;justify-content:center;gap:9px;font-weight:700;color:var(--blue-deep);z-index:2}
.brand .dot{width:18px;height:18px;border-radius:50%;background:var(--orange)}
.brand-name{font-size:26px;line-height:1}
.tagline{position:absolute;top:200px;left:20px;right:20px;text-align:center;font-size:10.5px;font-weight:700;font-style:italic;color:var(--blue-deep);line-height:1.35;text-transform:uppercase}
.contact{position:absolute;left:0;right:0;text-align:center;font-size:16px}
.icon-ring{width:30px;height:30px;border:2px solid var(--orange);border-radius:50%;display:flex;align-items:center;justify-content:center;margin:0 auto 6px}
.socials{position:absolute;top:403px;left:0;right:0;display:flex;justify-content:center;gap:14px}
.socials span{width:20px;height:20px;border:2px solid var(--blue);border-radius:50%}
.notes{position:absolute;left:23px;top:499px;width:325px;height:201px;border:3px solid var(--green);border-radius:22px;display:flex;align-items:center;justify-content:center;font-size:36px;color:#bbb}
.cover-title{position:absolute;top:36px;left:0;right:0;text-align:center;font-family:'Oswald',sans-serif;line-height:1.12;font-weight:400}
.cover-title .l1{font-size:38px;color:#333}
.cover-title .l2{font-size:44px;font-weight:500}
.cover-title .w1{color:var(--blue)}.cover-title .w2{color:var(--green)}
.photo{position:absolute;z-index:1}
.photo-rails{top:185px;left:0;right:0;height:414px;background:linear-gradient(180deg,#f2d7a0,#a8a37a 45%,#6a6257);border-bottom:5px solid var(--green)}
.pill{position:absolute;top:24px;left:50%;transform:translateX(-50%);white-space:nowrap;border-radius:30px;padding:6px 22px;color:#fff;font-family:'Oswald',sans-serif;font-weight:400;font-size:22px;line-height:1.2;box-shadow:0 3px 4px rgba(0,0,0,.2);text-align:center}
.pill-green{background:var(--green)}.pill-orange{background:var(--orange)}
.pill-blue{background:var(--blue-deep);width:334px;padding:7px 10px;font-size:17px}
.pill-blue.small{font-size:14px;padding:9px 10px}
.benefits{position:absolute;top:88px;left:16px;right:22px;list-style:none}
.benefits li{position:relative;padding-left:22px;margin-bottom:8px}
.benefits li::before{content:"";position:absolute;left:1px;top:2px;width:11px;height:6px;border-left:3px solid var(--orange);border-bottom:3px solid var(--orange);transform:rotate(-45deg)}
.benefit-title{font-family:'Oswald',sans-serif;font-size:13.5px;line-height:1.3;color:var(--blue-deep);text-transform:uppercase}
.benefit-copy{font-size:10.5px;line-height:1.3;text-align:justify;color:var(--muted)}
.step-ring{position:absolute;left:50%;width:62px;height:62px;margin-left:-31px;border:3px solid var(--orange);border-radius:50%;display:flex;align-items:center;justify-content:center}
.step-label{position:absolute;left:0;right:0;text-align:center;font-size:14px;font-weight:700;color:var(--green-text);text-transform:uppercase}
.photo-group{top:413px;left:0;width:745px;height:311px;background:linear-gradient(180deg,#f4f4f4,#c9c2b8 40%,#6d7f8c)}
.photo-friends{top:435px;left:0;width:745px;height:289px;background:linear-gradient(90deg,#f3efe9,#dccab5 45%,#9a8a7a 75%,#e8e8e8)}
</style>
</head>
<body>

<section class="spread spread-cover">
  <div class="panel panel-left">
    <div class="brand" style="top:145px"><span class="dot"></span><span class="brand-name">BrimPath Wireless</span></div>
    <p class="tagline">From coast to coast,<br>BrimPath's nationwide wireless service area<br>has you covered</p>
    <div class="contact" style="top:268px">
      <div class="icon-ring"><svg width="14" height="14" viewBox="0 0 24 24"><path d="M6 2l4 5-2 3c1 3 3 5 6 6l3-2 5 4-3 4C10 22 2 14 2 5z" fill="var(--orange)"/></svg></div>
      800-555-0142
    </div>
    <div class="contact" style="top:330px">
      <div class="icon-ring"><svg width="14" height="12" viewBox="0 0 24 18"><rect x="1" y="1" width="22" height="16" fill="none" stroke="var(--orange)" stroke-width="2.5"/><path d="M1 1l11 9 11-9" fill="none" stroke="var(--orange)" stroke-width="2.5"/></svg></div>
      @brimpathwireless
    </div>
    <div class="socials"><span></span><span></span><span></span><span></span><span></span></div>
    <div class="notes">Space for notes</div>
    <div class="url-band band-blue">www.brimpathwireless-demo.com</div>
  </div>
  <div class="panel panel-right">
    <h1 class="cover-title"><span class="l1">WELCOME TO THE<br>NEW AGE OF</span><br><span class="l2"><span class="w1">WIRELESS</span> <span class="w2">SERVICE!</span></span></h1>
    <div class="photo photo-rails" role="img" aria-label="Photo of railway tracks running toward a sunset horizon"></div>
    <div class="brand" style="top:640px"><span class="dot"></span><span class="brand-name">BrimPath Wireless</span></div>
    <div class="url-band band-orange">www.brimpathwireless-demo.com</div>
  </div>
</section>

<section class="spread spread-inside-en">
  <div class="panel panel-left">
    <h2 class="pill pill-green">WHY BRIMPATH</h2>
    <ul class="benefits">
      <li><div class="benefit-title">Simple instant credit approval</div><p class="benefit-copy">With a 95+% approval rate, and an order which can be completed in under 5 minutes, BrimPath gets you on track in a way other carriers can't.</p></li>
      <li><div class="benefit-title">Stress free buying options</div><p class="benefit-copy">BrimPath takes the stress out of phone buying. We don't require everything to be paid up front to get talking, texting, or streaming!</p></li>
      <li><div class="benefit-title">Get your first month free</div><p class="benefit-copy">BrimPath provides you with a gift card so your first month is FREE! Never settle for less, choose BrimPath.</p></li>
      <li><div class="benefit-title">Best device protection available</div><p class="benefit-copy">Ever get your brand new phone and drop it? Scratch it? Lose it? Not only do BrimPath packages include headphones, car charger, and screen protector, they also include insurance at no additional cost. Need a little extra coverage? We have you covered with upgrade options at time of package selection.</p></li>
    </ul>
    <div class="url-band band-blue">www.brimpathwireless-demo.com</div>
  </div>
  <div class="panel panel-right">
    <h2 class="pill pill-blue">THREE SIMPLE STEPS TO YOUR NEW PHONE</h2>
    <div class="step-ring" style="top:80px"><svg width="20" height="30" viewBox="0 0 20 30"><rect x="2" y="2" width="16" height="26" rx="3" fill="none" stroke="var(--orange)" stroke-width="2.5"/></svg></div>
    <div class="step-label" style="top:150px">Choose phone &amp; plan</div>
    <div class="step-ring" style="top:185px"><svg width="26" height="20" viewBox="0 0 26 20"><path d="M3 10l7 7L23 3" fill="none" stroke="var(--orange)" stroke-width="3"/></svg></div>
    <div class="step-label" style="top:254px">Get financing</div>
    <div class="step-ring" style="top:289px"><svg width="26" height="26" viewBox="0 0 24 24"><path d="M2 10h4v12H2zM8 22h10l3-9v-3h-7l1-5-2-3-5 8z" fill="var(--orange)"/></svg></div>
    <div class="step-label" style="top:360px">Receive your phone in 3 days</div>
    <div class="url-band band-orange">www.brimpathwireless-demo.com</div>
  </div>
  <div class="photo photo-group" role="img" aria-label="Photo of a group of young friends on a sofa using phones and tablets"></div>
</section>

<section class="spread spread-inside-es">
  <div class="panel panel-left">
    <h2 class="pill pill-orange">¿POR QUÉ BRIMPATH?</h2>
    <ul class="benefits" style="top:90px">
      <li><div class="benefit-title">Simple aprobación instantánea de crédito</div><p class="benefit-copy">Con una tasa de aprobación de más del 95%, y una orden que se puede completar en menos de 5 minutos, BrimPath lo pone en marcha de una manera que otros proveedores no pueden.</p></li>
      <li><div class="benefit-title">Opciones de compromiso gratuitas</div><p class="benefit-copy">BrimPath elimina el estrés de la compra telefónica. ¡No necesitamos que todo se pague por adelantado para hablar, enviar mensajes de texto o transmitir!</p></li>
      <li><div class="benefit-title">Obtenga su primer mes gratis</div><p class="benefit-copy">¡BrimPath le proporciona una tarjeta de regalo para que su primer mes sea GRATIS! Nunca se conforme con menos, elija BrimPath.</p></li>
      <li><div class="benefit-title">La mejor protección de dispositivos disponible</div><p class="benefit-copy">¿Alguna vez tienes tu nuevo teléfono y lo dejas? ¿Rasguñalo? ¿Piérdelo? Los paquetes BrimPath no solo incluyen auriculares, cargador de coche y protector de pantalla, sino que también incluyen seguro sin costo adicional. ¿Necesita un poco de cobertura extra? Te cubrimos con opciones de actualización en el momento de la selección del paquete.</p></li>
    </ul>
    <div class="url-band band-blue">www.brimpathwireless-demo.com</div>
  </div>
  <div class="panel panel-right">
    <h2 class="pill pill-blue small">TRES PASOS SENCILLOS PARA SU NUEVO TELÉFONO</h2>
    <div class="step-ring" style="top:82px"><svg width="20" height="30" viewBox="0 0 20 30"><rect x="2" y="2" width="16" height="26" rx="3" fill="none" stroke="var(--orange)" stroke-width="2.5"/></svg></div>
    <div class="step-label" style="top:152px">Elija el teléfono y el plan</div>
    <div class="step-ring" style="top:186px"><svg width="26" height="20" viewBox="0 0 26 20"><path d="M3 10l7 7L23 3" fill="none" stroke="var(--orange)" stroke-width="3"/></svg></div>
    <div class="step-label" style="top:256px">Obtener financiamiento</div>
    <div class="step-ring" style="top:290px"><svg width="26" height="26" viewBox="0 0 24 24"><path d="M2 10h4v12H2zM8 22h10l3-9v-3h-7l1-5-2-3-5 8z" fill="var(--orange)"/></svg></div>
    <div class="step-label" style="top:362px">Recibe su teléfono en 3 días</div>
    <div class="url-band band-orange">www.brimpathwireless-demo.com</div>
  </div>
  <div class="photo photo-friends" role="img" aria-label="Photo of two friends laughing while talking on a phone"></div>
  <div class="brand" style="top:502px;right:auto;width:372px"><span class="dot"></span><span class="brand-name">BrimPath Wireless</span></div>
</section>

</body>
</html>
```